RW Talbrook LLC Business Card - Civil Engineering & Consulting Firm

We need a Business Card that is elegant, and masculine.  It is our Professional Civil Engineering & Consulting Company located in San Antonio TX (Not s construction or builder firm- no gears & no tool images please). We provide civil engineering services including  commercial site plans, grading and drainage plans, utility plans, hydraulics and hydrology, land planning, utility coordination, and other general civil engineering services related to commercial and residential development.
We have 2 existing Logos. We would like to convey reliability, strength, trustworthiness and attention to detail.  Blues and orange tones as per logo We are OK with the use of a darker blue in the mix.  We have 2 logo versions - Full Company Name Logo to go on the back of card, & Small Icon Logo for the front w/ personal Info.

Target Market(s)
Architects, Real Estate Developers, Other Strctural Engineers, Surveyers, General Contractors
Industry/Entity Type
Professional Civil Engineering
Contact Information for Business Card
Name, Position, Address, Cell & Office #, email, and company website
Font styles to use
Other font styles liked:
- Avian
Requirements
Should not have
- No Tools, No Gears, no Cranes, or Construction Equipment.

```html
<!DOCTYPE html>
<html lang="en">
<head>
<meta charset="utf-8">
<title>RW Talbrook LLC – Business Card</title>
<link rel="stylesheet" href="https://fonts.googleapis.com/css2?family=Rubik:wght@400;500&display=swap">
<style>
  :root{
    --backdrop:#e4e4e4;
    --card:#ffffff;
    --blue:#6fa3d4;
    --orange:#f08a2c;
    --ink:#5a5a5a;
    --rule:#c9c9c9;
  }
  *{box-sizing:border-box;margin:0;padding:0}
  html,body{width:1200px;height:1200px;overflow:hidden}
  body{background:var(--backdrop);font-family:"Rubik",Arial,sans-serif;position:relative}
  .card{position:absolute;left:262px;width:686px;height:392px;background:var(--card)}
  .card--front{top:165px}
  .card--back{top:653px}

  .front-brand{position:absolute;left:0;top:0;width:286px;height:100%;
    display:flex;align-items:center;justify-content:center;gap:10px}
  .brand-mark{width:14px;height:14px;background:var(--orange)}
  .brand-name{font-size:24px;font-weight:500;color:var(--blue);letter-spacing:.5px}
  .divider{position:absolute;left:286px;top:87px;width:1px;height:240px;background:var(--rule)}

  .contact{position:absolute;left:320px;top:106px;color:var(--ink)}
  .contact__name{font-size:26px;font-weight:500;color:var(--blue);letter-spacing:.6px;line-height:1.1}
  .contact__role{font-size:17px;color:var(--orange);line-height:1.2;margin-bottom:8px}
  .contact__address{font-size:17px;line-height:1.3;margin-bottom:8px}
  .contact__list{list-style:none}
  .contact__list li{display:flex;align-items:center;gap:10px;font-size:17px;line-height:21px}
  .contact__list svg{width:13px;height:13px;flex:none;fill:var(--orange)}

  .back-brand{position:absolute;inset:0;display:flex;align-items:center;justify-content:center;gap:14px}
  .back-brand .brand-mark{width:22px;height:22px}
  .back-brand .brand-name{font-size:48px;font-weight:400;letter-spacing:2px}
</style>
</head>
<body>
  <section class="card card--front">
    <div class="front-brand">
      <span class="brand-mark"></span>
      <span class="brand-name">RW Talbrook</span>
    </div>
    <div class="divider"></div>
    <div class="contact">
      <p class="contact__name">DANIEL HARTWELL</p>
      <p class="contact__role">President</p>
      <p class="contact__address">4210 Cedar Ridge Road<br>San Antonio, Texas 78216</p>
      <ul class="contact__list">
        <li><svg viewBox="0 0 16 16" aria-hidden="true"><path d="M3 1l3 3-1.5 2a9 9 0 0 0 5.5 5.5L12 10l3 3-2 2C7 15 1 9 1 3z"/></svg>123-456-7890</li>
        <li><svg viewBox="0 0 16 16" aria-hidden="true"><path d="M4 0h8v16H4zM5.5 2v10h5V2z"/></svg>123-456-7890</li>
        <li><svg viewBox="0 0 16 16" aria-hidden="true"><path d="M1 4h14v9H1zM2.5 5.5L8 9.5l5.5-4z"/></svg>hartwell@rwtalbrook.com</li>
        <li><svg viewBox="0 0 16 16" aria-hidden="true"><circle cx="8" cy="8" r="7"/></svg>www.rwtalbrook.com</li>
      </ul>
    </div>
  </section>

  <section class="card card--back">
    <div class="back-brand">
      <span class="brand-mark"></span>
      <span class="brand-name">RW Talbrook LLC</span>
    </div>
  </section>
</body>
</html>
```